Creative Business Card for my Sail Boat.. Tide & Drift

Going to order PLASTIC business cards for my boat.. she is a sailing vessel catamaran named Tide & Drift..

Target Market(s)

to impress other boaters with a unique designed plastic card

Contact Information for Business Card

S/V Tide & Drift
Captain Carl Denby
denby@carl.example
Mobile/WhatsApp 1-555-318-7620
www.sailtideanddrift.example

Requirements
Must have
• Cool colors. logo.. and info in Business Card Details.. Thanks! Utilize clear or cloudy plastic in design. Thanks

```html
<!DOCTYPE html>
<html lang="en">
<head>
<meta charset="utf-8">
<title>Tide &amp; Drift – Business Card</title>
<link href="https://fonts.googleapis.com/css2?family=Lato:wght@400;700;900&display=swap" rel="stylesheet">
<style>
  :root {
    --backdrop: #e9e1d6;
    --card-frost: #eee7de;
    --card-edge: rgba(255,255,255,0.75);
    --brown-deep: #4a1f0c;
    --brown-band: #55260f;
    --swoosh: #b7aba0;
    --swoosh-light: #d9d0c6;
    --name-brown: #4e1e0b;
    --title-grey: #6c5e55;
    --logo-brown: #6e5446;
    --contact-text: #efe4d8;
  }
  * { margin: 0; padding: 0; box-sizing: border-box; }
  html, body {
    width: 1200px; height: 1047px; overflow: hidden;
    background: var(--backdrop);
    font-family: "Lato", sans-serif;
  }
  .card {
    position: absolute; left: 100px; top: 251px;
    width: 1000px; height: 545px;
    border-radius: 26px; overflow: hidden;
    background: linear-gradient(160deg, #f4efe8 0%, var(--card-frost) 55%, #e4dace 100%);
    border: 2px solid var(--card-edge);
    box-shadow: 0 10px 40px rgba(80,50,30,0.18);
  }
  .card__wave { position: absolute; inset: 0; width: 100%; height: 100%; }
  .holder { position: absolute; right: 62px; top: 78px; text-align: right; }
  .holder__name { font-weight: 900; font-size: 28px; color: var(--name-brown); letter-spacing: 0.3px; }
  .holder__title { font-weight: 400; font-size: 24px; color: var(--title-grey); margin-top: 12px; }
  .brand {
    position: absolute; left: 84px; top: 170px;
    display: flex; align-items: center; gap: 18px;
  }
  .brand__name { font-weight: 900; font-size: 70px; color: var(--logo-brown); letter-spacing: -1px; }
  .brand__dot { width: 34px; height: 34px; border-radius: 50%; background: var(--logo-brown); }
  .contact { position: absolute; right: 56px; top: 374px; list-style: none; }
  .contact__item {
    display: flex; justify-content: flex-end; align-items: center; gap: 26px;
    font-size: 24px; color: var(--contact-text); height: 44px;
  }
  .contact__icon { width: 24px; height: 24px; flex: none; }
</style>
</head>
<body>
  <div class="card">
    <svg class="card__wave" viewBox="0 0 1000 545" preserveAspectRatio="none" aria-hidden="true">
      <path d="M0 345 C140 440 320 425 500 370 C680 315 800 300 880 300 C790 305 660 340 500 395 C320 455 150 470 0 420 Z" fill="var(--swoosh)"/>
      <path d="M0 430 C160 465 320 450 500 405 C680 360 820 315 1000 312 L1000 545 L0 545 Z" fill="var(--swoosh-light)" opacity="0.7"/>
      <path d="M0 448 C170 478 330 462 510 415 C690 368 830 325 1000 322 L1000 545 L0 545 Z" fill="var(--brown-band)"/>
    </svg>

    <div class="holder">
      <div class="holder__name">CAPTAIN CARL DENBY</div>
      <div class="holder__title">Founder &amp; CEO</div>
    </div>

    <div class="brand">
      <span class="brand__name">Tide &amp; Drift</span>
      <span class="brand__dot"></span>
    </div>

    <ul class="contact">
      <li class="contact__item">1-555-318-7620
        <svg class="contact__icon" viewBox="0 0 24 24" fill="none" stroke="var(--contact-text)" stroke-width="2" stroke-linecap="round" stroke-linejoin="round"><path d="M5 3h4l2 5-2.5 1.5a11 11 0 0 0 6 6L16 13l5 2v4a2 2 0 0 1-2 2A16 16 0 0 1 3 5a2 2 0 0 1 2-2z"/></svg>
      </li>
      <li class="contact__item">denby@carl.example
        <svg class="contact__icon" viewBox="0 0 24 24" fill="none" stroke="var(--contact-text)" stroke-width="2" stroke-linejoin="round"><rect x="2" y="5" width="20" height="14" rx="1"/><path d="M2 6l10 7 10-7"/></svg>
      </li>
      <li class="contact__item">www.sailtideanddrift.example
        <svg class="contact__icon" viewBox="0 0 24 24" fill="none" stroke="var(--contact-text)" stroke-width="1.8"><circle cx="12" cy="12" r="10"/><ellipse cx="12" cy="12" rx="4.5" ry="10"/><path d="M2 12h20M4 7h16M4 17h16"/></svg>
      </li>
    </ul>
  </div>
</body>
</html>
```